Dashboard Elements

Hello – looking for someone to create dashboard elements.
I’ve already basically designed all these elements – but I need someone to take what I’ve designed and make it look like an actual dashboard UI, like an app - assuming using some kind of dashboard UI kit (but however you would like to get it done is fine). It can look just like mine or try something different, as long as it matches the color scheme webpage that I’m going to out it on – see the page here. I’m ok with making it dark, maybe that would look better – again as long as it matches the webpage (https://www.plankora.com/file/7QxVbN2kLmRtWp4Ya8Hc3J/Webpage-with-placeholders?node-id=0%3A1). Please note, you do not need to put anything on the webpage or do anything with this Figma file, this is just a reference so you can color/stylize it accordingly.

The attached Powerpoint file has everything you need - make sure to zoom all the way out to see everything on the slides.

Here are the Dashboard elements needed (this will all make sense when you look at the PPT):
Dashboard 1
Dashboard 1 – expanded view A
Dashboard 1 – expanded view B
View Source button by itself
Source Document Viewer 1 and 2 (these are exactly the same just with a different image inside)*
Dashboard 2 (only slightly different than Dashboard 1, just extended with extra headings
Table of Contents
Searchbar and Source Doc by itself
*the documents in the source document viewers should still look like documents - they don’t need to look like part of the UI, because this is a document viewer – you can restyle/recolor if necessary or just leave these as is.
- Colors must match color scheme of webpage, attached and on Figma link (images there currently are only placeholders) – ok to go dark as long as it matches
- Must look sleek, clean, realistic
- Don’t add any pictures of people or change the text.
- In case it’s not clear, this is what I mean by the concept of Dashboard UI - https://www.quillbary.com/shard/s2/sh/9a4c1e27-b835-4f02-a7d6-5c0e81b3f947/e72b6a09c4d1f5830b9e6a2d7c4f1e58
- Must be sent in an editable file, I may need to be edit text and other elements
- If you are going to send a sample, please make sure it’s part of the dashboard itself, not just the table of contents etc

Ideally hoping to find someone I can continue working with as I'll have a lot more graphic design work needed coming up.

Thank you!

```html
<!DOCTYPE html>
<html lang="en">
<head>
<meta charset="utf-8">
<title>Dashboard Elements</title>
<link href="https://fonts.googleapis.com/css2?family=Rajdhani:wght@300;400;500;600;700&display=swap" rel="stylesheet">
<style>
:root{
  --bg:#110c22;
  --card:#1b1634;
  --card-edge:#2c2550;
  --band:#261f48;
  --row-line:#2a2349;
  --overlay:#29234f;
  --overlay-edge:#5a4f9c;
  --teal:#1ec9bf;
  --violet:#8b80f2;
  --violet-edge:#4f4690;
  --text:#e9e6f5;
  --muted:#b4aed0;
  --dim:#8a84a6;
}
*{box-sizing:border-box;margin:0;padding:0}
html,body{width:1200px;height:1117px;overflow:hidden;background:var(--bg)}
body{position:relative;font-family:"Rajdhani",sans-serif;color:var(--text)}
.abs{position:absolute}
.section-title{position:absolute;font-weight:300;font-size:24px;letter-spacing:.5px;color:#f2f0fa}
.brand{display:flex;align-items:center;gap:5px;font-weight:500;color:var(--text);letter-spacing:.3px}
.brand .mark{display:inline-block;background:var(--teal)}
.teal{color:var(--teal)}

/* Dashboard card */
.hcc-card{left:95px;top:64px;width:388px;height:270px;background:var(--card);border:2px solid var(--card-edge);border-radius:10px;overflow:hidden;box-shadow:6px 6px 0 #241d44}
.hcc-card .brand{position:absolute;left:16px;top:18px;font-size:12px}
.hcc-card .brand .mark{width:9px;height:9px}
.hcc-card .doc-name{position:absolute;left:140px;top:20px;font-size:8px;color:var(--muted)}
.hcc-card .pt-meta{position:absolute;right:22px;top:14px;text-align:right;font-size:5.5px;line-height:7px;color:var(--muted)}
.hcc-card .summary{position:absolute;left:16px;top:52px;font-size:7px;color:var(--muted)}
.hcc-card .summary b{color:var(--teal);font-size:6px;margin-right:3px}
.hcc-card .stats{position:absolute;right:22px;top:50px;font-size:8.5px;color:var(--muted)}
.hcc-table{position:absolute;left:0;top:80px;width:100%}
.hcc-row{display:grid;grid-template-columns:69px 160px 70px 62px;align-items:center;height:32px;padding-left:16px;border-bottom:1px solid var(--row-line);font-size:7px;color:var(--muted)}
.hcc-row.head{height:30px;background:var(--band);border:0;color:var(--text);font-size:7.5px}
.hcc-row .code{color:var(--teal);font-size:6px}
.hcc-row .count{text-align:center}
.hcc-row .raf{color:var(--teal);text-align:right;padding-right:6px;white-space:nowrap}
.hcc-row .raf::after{content:"▾";font-size:6px;margin-left:3px}
.hcc-row.head .count,.hcc-row.head .raf{color:var(--text)}
.hcc-row.head .raf{padding-right:14px}
.hcc-row.head .raf::after{content:""}

/* Table of content */
.toc{width:121px;font-size:8px}
.toc .toc-head{height:22px;background:var(--card);border:1px solid var(--card-edge);border-radius:3px;display:flex;align-items:center;justify-content:space-between;padding:0 10px;margin-bottom:3px}
.toc .toc-head::after{content:"▾";color:var(--teal);font-size:7px}
.toc ul{list-style:none;border:1px solid var(--card-edge);border-radius:3px;overflow:hidden;background:var(--card)}
.toc li{display:flex;align-items:center;padding-left:10px;border-bottom:2px solid var(--bg)}
.toc li:last-child{border-bottom:0}
.toc li.active{background:var(--teal);color:#eafffd}
.toc-a{left:548px;top:56px}
.toc-a li{height:23px}
.toc-b{left:703px;top:56px}
.toc-b li{height:21.5px;border-bottom:1px solid var(--row-line)}

/* Expanded card */
.expanded{left:168px;top:438px;width:402px;height:290px;background:var(--card);border:1px solid var(--card-edge);border-radius:10px}
.exp-top{display:grid;grid-template-columns:82px 196px 60px 1fr;align-items:center;height:28px;padding:0 22px 0 24px;border-bottom:1px solid var(--row-line);font-size:7px;color:var(--text)}
.exp-top .code{color:var(--teal)}
.exp-top .raf{color:var(--teal);text-align:right;white-space:nowrap}
.exp-top .raf::after{content:"▾";font-size:5px;margin-left:2px}
.why{position:absolute;left:24px;top:42px;font-size:6px;color:var(--text)}
.why b{font-weight:700}
.evidence{position:absolute;display:flex;align-items:center;height:54px;font-size:8px}
.evidence .label{font-weight:700;line-height:12px}
.evidence .src{color:var(--teal);font-weight:600;font-size:7.5px}
.evidence .src-detail{font-size:7px;line-height:12px;color:var(--text)}
.evidence.flat{left:0;width:400px;background:#1f1a3c;padding-left:23px}
.evidence.raised{background:var(--overlay);border:1px solid var(--overlay-edge);border-radius:5px}
.view-src{position:absolute;display:flex;align-items:center;justify-content:center;gap:5px;width:94px;height:28px;border:1px solid var(--violet-edge);border-radius:4px;background:#241e46;color:var(--violet);font-weight:700;font-size:8.5px;letter-spacing:.3px}
.view-src svg{width:10px;height:12px}

/* Source document */
.source-doc{left:665px;top:401px;width:452px;height:674px;background:var(--card);border:2px solid var(--card-edge);border-radius:14px;font-size:8.5px}
.source-doc .inner{position:absolute;left:24px;top:0;right:24px}
.source-doc .brand{position:absolute;top:18px;font-size:14.5px}
.source-doc .brand .mark{width:13px;height:13px}
.source-doc .intro{position:absolute;top:49px;color:var(--muted);font-size:8.5px}
.facts{position:absolute;top:95px;font-size:9.5px;line-height:16.8px}
.facts div{display:grid;grid-template-columns:142px 200px}
.facts .label{font-weight:500}
.facts .value{color:#d6d2e6}
.facts .gap{margin-top:17px}
.block{position:absolute;left:0}
.block .cap{font-size:7.5px;color:var(--dim);margin-bottom:3px}
.block p{line-height:13px;color:#dcd8ea;font-size:8.5px}
.mini{display:grid;font-size:8px;line-height:13.5px}
.mini .h{color:var(--teal);font-weight:600}
.mini span{color:#d6d2e6}
.va-table{position:absolute;left:0;width:375px;height:53px;border:1px solid #3b3465;border-radius:4px;font-size:8px;color:#d6d2e6}
.va-table span{position:absolute}
.va-table .rule{position:absolute;left:0;right:0;top:37px;border-top:1px solid #3b3465}
</style>
</head>
<body>

<h1 class="section-title" style="left:210px;top:20px">Dashboard 1</h1>

<section class="abs hcc-card" aria-label="HCC summary dashboard">
  <div class="brand"><span class="mark"></span>CLARIVEX</div>
  <div class="doc-name">C-CDA Compendium</div>
  <div class="pt-meta">Patient, Ada<br>Female | 01/11/1951 | Age: 70</div>
  <div class="summary"><b>▼</b>HCC Summary</div>
  <div class="stats"><span class="teal">RAF: 2.362</span> | Condition Count: 8 &nbsp;| ID: 7326472</div>
  <div class="hcc-table">
    <div class="hcc-row head"><span>ICD-10 Code</span><span>Condition</span><span class="count">Condition</span><span class="raf">RAF</span></div>
    <div class="hcc-row"><span class="code">J44.9</span><span>Chronic obstructive pulmonary disease</span><span class="count">111</span><span class="raf">0.335</span></div>
    <div class="hcc-row"><span class="code">F33.1</span><span>Chronic kidney disease, moderate (stage 3)</span><span class="count">138</span><span class="raf">0.069</span></div>
    <div class="hcc-row"><span class="code">J44.9</span><span>Major depressive disorder, recurrent, mild</span><span class="count">59</span><span class="raf">0.335</span></div>
    <div class="hcc-row"><span class="code">I42.9</span><span>Cardiomyopathy</span><span class="count">85</span><span class="raf">0.447</span></div>
    <div class="hcc-row"><span class="code">E11.36</span><span>Type 2 diabetes mellitus with diabetic cataract</span><span class="count">18</span><span class="raf">0.302</span></div>
  </div>
</section>

<nav class="abs toc toc-a">
  <div class="toc-head">Table of Content</div>
  <ul>
    <li class="active">Insurance Provider</li><li>Problems</li><li>Results</li><li>Procedures</li><li>Encounters</li><li>Medications</li><li>Vital Signs</li><li>Immunizations</li><li>Social History</li><li>Family History</li><li>Plan of Care</li>
  </ul>
</nav>

<nav class="abs toc toc-b">
  <div class="toc-head">Table of Content</div>
  <ul>
    <li class="active">Insurance Provider</li><li>Problems</li><li>Results</li><li>Procedures</li><li>Encounters</li><li>Medications</li><li>Vital Signs</li><li>Immunizations</li><li>Social History</li><li>Family History</li><li>Plan of Care</li>
  </ul>
</nav>

<h2 class="section-title" style="left:250px;top:392px">Dashboard 1 – expanded</h2>

<svg width="0" height="0" style="position:absolute">
  <symbol id="doc-icon" viewBox="0 0 10 12"><path d="M1 .5h5.5L9 3v8.5H1z" fill="none" stroke="currentColor" stroke-width=".9"/><path d="M6.5.5V3H9M3 5.5h4M3 7.3h4M3 9.1h4" fill="none" stroke="currentColor" stroke-width=".8"/></symbol>
</svg>

<section class="abs expanded" aria-label="Expanded condition detail">
  <div class="exp-top"><span class="code">F33.1</span><span>Type 2 diabetes mellitus with diabetic cataract</span><span>18</span><span class="raf">0.069</span></div>
  <div class="why"><b>Why:</b> This patient has an eGFR between 45-59 mL/min</div>

  <div class="evidence flat" style="top:73px">
    <span class="label" style="width:102px">Extracapsular<br>Cataract with IOL</span>
    <span class="src">C-CDA: PROCEDURES</span>
  </div>
  <div class="view-src" style="left:285px;top:86px"><svg><use href="#doc-icon"/></svg>VIEW SOURCE</div>

  <div class="evidence flat" style="top:181px">
    <span class="label" style="width:102px">Diabetes type 2</span>
    <span class="src">C-CDA: PROBLEM LIST</span>
  </div>
  <div class="view-src" style="left:285px;top:194px"><svg><use href="#doc-icon"/></svg>VIEW SOURCE</div>
</section>

<div class="evidence raised" style="left:226px;top:565px;width:402px;padding-left:22px">
  <span class="label" style="width:102px">Cataract</span>
  <span><span class="src">Ophthalmology Chart Note</span><br><span class="src-detail">Patient presents for cataract<br>evaluation in the right eye.</span></span>
</div>
<div class="view-src" style="left:511px;top:579px"><svg><use href="#doc-icon"/></svg>VIEW SOURCE</div>

<div class="evidence raised" style="left:106px;top:674px;width:403px;padding-left:22px">
  <span class="label" style="width:102px">HbA1c</span>
  <span><span class="src">Lab Results</span><br><span class="src-detail">Hemoglobin A1C<br>6.9% 01/15/21</span></span>
</div>
<div class="view-src" style="left:392px;top:688px"><svg><use href="#doc-icon"/></svg>VIEW SOURCE</div>

<section class="abs source-doc" aria-label="Source document viewer">
  <div class="inner">
    <div class="brand"><span class="mark"></span>CLARIVEX</div>
    <div class="intro">Lorem ipsum dolor sit amet, consectetur adipiscing elit, sed do eiusmod tempor incididunt ut</div>

    <div class="facts">
      <div><span class="label">PATIENT :</span><span class="value">Ada Sample</span></div>
      <div><span class="label">DATE OF BIRTH :</span><span class="value">01/11/1951</span></div>
      <div><span class="label">DATE :</span><span class="value">04/02/2021 4:00 PM</span></div>
      <div><span class="label">DOCUMENT TYPE :</span><span class="value">Ophthalmology Chart Note</span></div>
      <div><span class="label">VISIT TYPE :</span><span class="value">Office Visit</span></div>
      <div class="gap"><span class="label">Referring Doctor :</span><span class="value">Owen Hartley</span></div>
    </div>

    <div class="block" style="top:236px">
      <div class="cap">General</div>
      <p>Patient Visit : Established Patient</p>
    </div>

    <div class="block" style="top:280px;width:350px">
      <div class="cap">History of Present Illness</div>
      <p>Lorem ipsum dolor sit amet, consectetur adipiscing elit, sed do eiusmod tempor incididunt ut labore et dolore magna aliqua. Ut enim ad minim veniam, quis nostrud exercitation ullamco laboris nisi ut aliquip ex ea commodo consequat.</p>
    </div>

    <div class="block" style="top:350px">
      <div class="cap">Past Ocular History</div>
      <div class="mini" style="grid-template-columns:59px 45px 60px 69px 59px 80px">
        <span class="h">Disease</span><span class="h">Eye</span><span class="h">Date Dx</span><span class="h">Procedure</span><span class="h">Date Px</span><span class="h">Surgeon</span>
        <span>Cataract</span><span>OS</span><span>04/15/2019</span><span>Phaco-PCIOL</span><span>06/23/2019</span><span>Lena Brandt MD.</span>
      </div>
    </div>

    <div class="block" style="top:407px">
      <div class="cap">Review of Systems</div>
      <div class="mini" style="grid-template-columns:59px 62px 60px">
        <span class="h">System</span><span class="h">Neg/Pos</span><span class="h">Details</span>
        <span>Cataract</span><span>Negative</span><span>Negative</span>
        <span>Eyes</span><span>Negative</span><span>Negative</span>
      </div>
    </div>

    <div class="block" style="top:477px">
      <div class="cap">Visual Acuity</div>
      <div class="mini" style="grid-template-columns:74px 85px 40px">
        <span class="h">Va OD</span><span class="h">Distance</span><span class="h">Near</span>
      </div>
    </div>
    <div class="va-table" style="top:507px">
      <span style="left:7px;top:4px">Dva</span><span style="left:26px;top:4px">cc</span><span style="left:43px;top:4px">mod</span><span style="left:72px;top:4px">mod</span><span style="left:101px;top:4px">Dva</span><span style="left:121px;top:4px">ph</span><span style="left:136px;top:4px">mod</span><span style="left:165px;top:4px">Dva</span><span style="left:191px;top:4px">Nva</span><span style="left:211px;top:4px">cc</span><span style="left:226px;top:4px">mod</span><span style="left:255px;top:4px">Nva</span><span style="left:275px;top:4px">cc</span><span style="left:290px;top:4px">mod</span><span style="left:319px;top:4px">Nva</span><span style="left:339px;top:4px">cc</span><span style="left:354px;top:4px">mod</span>
      <span style="left:101px;top:20px">sc</span><span style="left:165px;top:20px">Other</span>
      <div class="rule"></div>
      <span style="left:101px;top:40px">20/30</span><span style="left:131px;top:40px">-1</span>
    </div>

    <div class="block" style="top:583px">
      <div class="mini" style="grid-template-columns:74px 85px 40px">
        <span class="h">Va OS</span><span class="h">Distance</span><span class="h">Near</span>
      </div>
    </div>
    <div class="va-table" style="top:600px">
      <span style="left:7px;top:4px">Dva</span><span style="left:26px;top:4px">cc</span><span style="left:43px;top:4px">mod</span><span style="left:72px;top:4px">mod</span><span style="left:101px;top:4px">Dva</span><span style="left:121px;top:4px">ph</span><span style="left:136px;top:4px">mod</span><span style="left:165px;top:4px">Dva</span><span style="left:191px;top:4px">Nva</span><span style="left:211px;top:4px">cc</span><span style="left:226px;top:4px">mod</span><span style="left:255px;top:4px">Nva</span><span style="left:275px;top:4px">cc</span><span style="left:290px;top:4px">mod</span><span style="left:319px;top:4px">Nva</span><span style="left:339px;top:4px">cc</span><span style="left:354px;top:4px">mod</span>
      <span style="left:101px;top:20px">sc</span><span style="left:165px;top:20px">Other</span>
      <div class="rule"></div>
      <span style="left:101px;top:40px">20/30</span><span style="left:131px;top:40px">-1</span>
    </div>
  </div>
</section>

</body>
</html>
```